Business Card for IT company

I need a high tech looking business card using our logo. I prefer something clean and modern.

Target Market(s)

Buyers of IT hardware and software, IT Techies who are key influencers

Industry/Entity Type

Business

```html
<!DOCTYPE html>
<html lang="en">
<head>
<meta charset="utf-8">
<title>QBRX Consulting – Business Card</title>
<link href="https://fonts.googleapis.com/css2?family=Arimo:wght@400;700&family=Comfortaa:wght@700&display=swap" rel="stylesheet">
<style>
  :root {
    --backdrop: #1f1f1f;
    --card-light: #f6f6f6;
    --card-mid: #e7e7e7;
    --ink: #2b2b2b;
    --ink-soft: #3a3a3a;
    --brand-green: #3db14a;
    --white: #ffffff;
    --cluster-light: #d4d4d4;
    --cluster-dark: #4a4a4a;
  }
  * { margin: 0; padding: 0; box-sizing: border-box; }
  html, body {
    width: 1200px;
    height: 1000px;
    overflow: hidden;
    background: var(--backdrop);
  }
  .card {
    position: absolute;
    left: 75px;
    top: 200px;
    width: 1050px;
    height: 600px;
    overflow: hidden;
    background:
      repeating-linear-gradient(178deg, rgba(255,255,255,0.35) 0 1px, rgba(0,0,0,0.02) 1px 3px),
      linear-gradient(180deg, var(--card-light), var(--card-mid));
  }
  .brand {
    position: absolute;
    left: 58px;
    top: 44px;
    display: flex;
    align-items: flex-start;
    gap: 16px;
    font-family: "Arimo", Arial, sans-serif;
    color: var(--ink-soft);
  }
  .brand-name {
    display: flex;
    flex-direction: column;
    line-height: 1;
  }
  .brand-word {
    font-weight: 700;
    font-size: 100px;
    letter-spacing: -2px;
  }
  .brand-tag {
    font-weight: 400;
    font-size: 30px;
    letter-spacing: 11px;
    margin-top: 8px;
  }
  .brand-mark {
    width: 22px;
    height: 22px;
    margin-top: 58px;
    background: var(--brand-green);
  }
  .name-band {
    position: absolute;
    left: 0;
    top: 178px;
    width: 515px;
    height: 108px;
    background: var(--brand-green);
    clip-path: polygon(0 0, 450px 0, 100% 100%, 0 100%);
  }
  .person-name {
    position: absolute;
    left: 58px;
    top: 186px;
    font-family: "Comfortaa", "Trebuchet MS", sans-serif;
    font-weight: 700;
    font-size: 44px;
    line-height: 1.2;
    color: var(--white);
  }
  .person-title {
    position: absolute;
    left: 60px;
    top: 246px;
    font-family: "Arimo", Arial, sans-serif;
    font-weight: 700;
    font-size: 22px;
    line-height: 1.2;
    color: var(--ink);
  }
  .contact {
    position: absolute;
    left: 50px;
    top: 318px;
    list-style: none;
    font-family: "Arimo", Arial, sans-serif;
    font-weight: 700;
    font-size: 30px;
    color: var(--ink);
    line-height: 50px;
    letter-spacing: 1.5px;
  }
  .tech-cluster {
    position: absolute;
    left: 560px;
    top: 0;
    width: 490px;
    height: 600px;
    background: linear-gradient(100deg, var(--cluster-light) 0%, #8a8a8a 45%, var(--cluster-dark) 100%);
  }
</style>
</head>
<body>
  <section class="card">
    <div class="brand">
      <div class="brand-name">
        <span class="brand-word">QBRX</span>
        <span class="brand-tag">CONSULTING</span>
      </div>
      <span class="brand-mark"></span>
    </div>

    <div class="name-band"></div>
    <p class="person-name">Alan Pryce</p>
    <p class="person-title">Director</p>

    <ul class="contact">
      <li>202.555.0148 Office</li>
      <li>apryce@qbrx.com</li>
      <li>www.QBRX.com</li>
    </ul>

    <div class="tech-cluster" role="img" aria-label="Collage of dark technology icons such as gears, wifi, links, at-signs, devices and user symbols, with dotted arrows"></div>
  </section>
</body>
</html>
```